Cybersecurity company is looking for business card.

I need a business card design for our company, we are a cybersecurity company providing advance technology to protect agains any kind of malware. We need a fresh modern design it should communicate modern, technology and growth.

Target Market(s)

Business to business

Industry/Entity Type

Business

Contact Information for Business Card

Should have location, address, fax, mobile, phone, email and website.

Requirements
Must have
• Must follow company's logo color and style. Must have the company's log on its.

```html
<!DOCTYPE html>
<html lang="en">
<head>
<meta charset="utf-8">
<title>Vexlon Business Card</title>
<link rel="stylesheet" href="https://fonts.googleapis.com/css2?family=Saira:wght@400;500;700&display=swap">
<style>
  :root {
    --backdrop: #e9e6e2;
    --brand-red: #a11c24;
    --brand-red-light: #c8242d;
    --brand-red-dark: #8e161d;
    --ink: #111111;
    --ink-soft: #2a2a2a;
    --card-white: #ffffff;
    --pattern-grey: #cfcfcf;
  }
  * { box-sizing: border-box; margin: 0; padding: 0; }
  html, body {
    width: 1200px;
    height: 1000px;
    overflow: hidden;
    background: var(--backdrop);
    font-family: "Saira", "Helvetica Neue", Arial, sans-serif;
  }
  .canvas { position: relative; width: 1200px; height: 1000px; }

  .card {
    position: absolute;
    left: 265px;
    width: 667px;
    height: 397px;
    overflow: hidden;
    box-shadow: 0 6px 16px rgba(0,0,0,0.18);
  }

  /* Front side */
  .card--front { top: 73px; background: var(--brand-red); }
  .card--front .pattern-fill {
    position: absolute; inset: 0;
    background: linear-gradient(135deg, var(--brand-red-light) 0%, var(--brand-red) 45%, var(--brand-red-dark) 100%);
  }
  .front-wordmark {
    position: absolute;
    left: 195px; top: 208px;
    width: 380px;
    text-align: center;
    color: var(--card-white);
    font-weight: 700;
    font-size: 92px;
    line-height: 1;
    letter-spacing: 1px;
  }
  .front-web {
    position: absolute;
    left: 195px; top: 309px;
    width: 380px;
    text-align: center;
    color: var(--card-white);
    font-weight: 500;
    font-size: 17px;
    letter-spacing: 0.5px;
  }

  /* Back side */
  .card--back { top: 533px; background: var(--card-white); }
  .card--back .pattern-fill { position: absolute; left: 0; top: 0; }
  .back-wordmark {
    position: absolute;
    left: 312px; top: 44px;
    color: var(--ink);
    font-weight: 700;
    font-size: 70px;
    line-height: 1;
    letter-spacing: 1px;
  }
  .details { position: absolute; left: 313px; top: 148px; color: var(--ink); }
  .person-name { color: var(--brand-red); font-size: 29px; font-weight: 400; line-height: 1; }
  .person-role { font-size: 16px; color: var(--ink-soft); line-height: 1.2; margin-top: 2px; }
  .address { margin-top: 14px; font-size: 16px; font-weight: 500; line-height: 22px; }
  .contact-list { list-style: none; margin-top: 10px; }
  .contact-list li {
    display: flex; align-items: center; gap: 6px;
    font-size: 17px; line-height: 23px; letter-spacing: 0.3px;
  }
  .contact-list li.email { font-size: 16px; margin-top: 2px; }
  .contact-list svg { width: 15px; height: 15px; fill: var(--brand-red); flex: none; }
</style>
</head>
<body>
<main class="canvas">

  <section class="card card--front" aria-label="Card front">
    <div class="pattern-fill" role="img" aria-label="Red geometric triangle grid pattern"></div>
    <div class="front-wordmark">vexlon</div>
    <div class="front-web">www.vexlon.com</div>
  </section>

  <section class="card card--back" aria-label="Card back">
    <svg class="pattern-fill" width="667" height="397" viewBox="0 0 667 397" role="img" aria-label="Fading grey geometric triangle pattern">
      <defs>
        <linearGradient id="greyFade" x1="0" y1="0" x2="1" y2="1">
          <stop offset="0" stop-color="#cfcfcf" stop-opacity="0.75"/>
          <stop offset="0.6" stop-color="#dedede" stop-opacity="0.45"/>
          <stop offset="1" stop-color="#ffffff" stop-opacity="0"/>
        </linearGradient>
      </defs>
      <polygon points="0,0 300,0 0,300" fill="url(#greyFade)"/>
    </svg>

    <div class="back-wordmark">vexlon</div>

    <div class="details">
      <h1 class="person-name">John Doe</h1>
      <p class="person-role">General Manager</p>
      <p class="address">Harbor Tech Park (HTP)<br>Meridian Avenue</p>
      <ul class="contact-list">
        <li>
          <svg viewBox="0 0 16 16" aria-hidden="true"><path d="M4 1h8a1 1 0 0 1 1 1v12a1 1 0 0 1-1 1H4a1 1 0 0 1-1-1V2a1 1 0 0 1 1-1zm1 2v9h6V3H5zm2.2 10a.8.8 0 1 0 1.6 0 .8.8 0 0 0-1.6 0z"/></svg>
          +100 55 555 XXXX
        </li>
        <li>
          <svg viewBox="0 0 16 16" aria-hidden="true"><path d="M1 6c0-2 3-3 7-3s7 1 7 3v1h-3.5V5.5h-7V7H1V6zm3 2h8l2 6H2l2-6zm4 1.5a2 2 0 1 0 0 4 2 2 0 0 0 0-4z"/></svg>
          07 555 XXXX
        </li>
        <li>
          <svg viewBox="0 0 16 16" aria-hidden="true"><path d="M4 1h8v4H4V1zM1 6h14v6h-3v3H4v-3H1V6zm4 4v3h6v-3H5z"/></svg>
          07 555 XXXX
        </li>
        <li class="email">
          <svg viewBox="0 0 16 16" aria-hidden="true"><path d="M1 3h14v10H1V3zm1.5 1.2L8 8.6l5.5-4.4H2.5z"/></svg>
          name.surname@vexlon.com
        </li>
      </ul>
    </div>
  </section>

</main>
</body>
</html>
```